Cannabis Processor Vape Cart Box Design/Concentrate Jar Box Design

We are a solventless (no chemicals added) cannabis processor in the state of Michigan. We have 2 products, one is a vape cartridge and one is a 5mL clear glass concentrate jar with a black lid. We need designs that correlates with our logo for their box packaging. Each piece of packaging has an opening so you can see the jar/vape cartridge and their contents. Each piece of packaging needs to have the universal symbol of cannabis, which is on the bottom right hand corner of the vape cartridge container for reference. Also on the jar box top lid we need the net weight listed like this (NET WT. 1.0g / 0.0176oz) I have attached some examples of the packaging boxes, the jar we will be using, and our logo so you know what you are shooting for. On the Jar Box there will be a hole in the center of the bottom of the box, so people can see the jar and it's contents. On the back of the jar box I would like the following (Here at 582 Resinworks, our mission is to be make the purest concentrates available. We strive to fully represent the true essence of the flower through our solventless processes. At 582 Resinworks we only use the finest Michigan grown, pesticide-free flowers for extraction. We pride ourselves on our chemical-free extraction methods, and are constantly innovating to bring better and cleaner concentrates for Medicinal and Recreational use.) On the Vape Cartridge box there will be a straight up and down hole in the shape of the vape cartridge instead of the Michigan shape. Get creative, but remember that you can not use any cannabis leaf symbol on the design. On the top of the back of the vape cartridge box I want the following (Here at 582 Resinworks, our mission is to be make the purest vape cartridge available. We strive to fully represent the true essence of the flower through our solventless processes. At 582 Resinworks we only use the finest Michigan grown, pesticide-free flowers for extraction. We pride ourselves on our chemical-free extraction methods, and are constantly innovating to bring better and cleaner products for both Medicinal and Recreational use.) We look forward to your submissions, and to the best design we thank you in advance. I almost forgot, we would prefer a black base with white lettering, but we are open to any creative ideas, so please submit more options than what we requested, because the best look will win.

```html
<!DOCTYPE html>
<html lang="en">
<head>
<meta charset="utf-8">
<title>582 Resinworks – Concentrate Jar Box</title>
<link rel="stylesheet" href="https://fonts.googleapis.com/css2?family=Barlow:ital,wght@0,500;0,600;0,700;1,500;1,700&display=swap">
<style>
  :root {
    --ink: #141414;
    --panel: #1a1a1a;
    --gold: #dbc154;
    --paper: #ffffff;
    --stage: #f4f4f2;
    --text-light: #f2f2f2;
  }
  * { margin: 0; padding: 0; box-sizing: border-box; }
  html, body {
    width: 1200px; height: 750px; overflow: hidden;
    background: var(--stage);
    font-family: "Barlow", sans-serif;
  }
  .canvas { position: relative; width: 1200px; height: 750px; }

  /* top lid */
  .lid {
    position: absolute; left: 60px; top: 70px;
    width: 600px; height: 170px;
    background: var(--gold);
  }

  /* front panel */
  .front {
    position: absolute; left: 60px; top: 240px;
    width: 600px; height: 380px;
    background: var(--panel);
  }
  .front svg, .side svg { position: absolute; left: 0; top: 0; overflow: visible; }

  .label {
    position: absolute; left: 150px; top: -60px;
    width: 300px; height: 150px;
    background: var(--paper);
    display: flex; flex-direction: column; align-items: center; justify-content: center;
    gap: 22px;
    box-shadow: 0 2px 4px rgba(0,0,0,.25);
  }
  .label-product {
    font-size: 8px; font-weight: 600; letter-spacing: 0.6em;
    color: var(--ink); text-align: center; line-height: 1.4;
    text-transform: uppercase;
  }
  .brand-name {
    font-size: 28px; font-weight: 600; color: var(--ink);
    letter-spacing: 0.04em;
  }

  .volume {
    position: absolute; left: 22px; top: 336px;
    font-size: 16px; font-weight: 700; color: var(--gold);
  }
  .product-name {
    position: absolute; left: 0; right: 0; top: 332px;
    text-align: center; color: var(--text-light);
    font-size: 13px; font-weight: 700; letter-spacing: 0.75em;
    line-height: 1.45; text-transform: uppercase;
  }
  .cannabis-mark {
    position: absolute; right: 36px; top: 316px;
    width: 60px; text-align: center;
  }
  .cannabis-mark .symbol {
    width: 20px; height: 20px; margin: 0 auto 5px;
    background: var(--gold);
  }
  .cannabis-mark .caption {
    font-size: 6px; font-weight: 700; letter-spacing: 0.3em;
    color: var(--text-light); line-height: 1.4;
  }

  /* side panel */
  .side {
    position: absolute; left: 680px; top: 240px;
    width: 460px; height: 380px;
    background: var(--panel);
  }
  .mission {
    position: absolute; left: 60px; top: 110px; width: 340px;
    font-size: 13px; font-weight: 500; font-style: italic;
    letter-spacing: 0.12em; line-height: 1.55;
    color: var(--text-light); text-align: center;
  }
  .mission em { font-style: italic; font-weight: 700; color: var(--gold); }
</style>
</head>
<body>
<main class="canvas">

  <div class="lid"></div>

  <section class="front">
    <svg width="600" height="380" viewBox="0 0 600 380" aria-hidden="true">
      <g stroke="var(--gold)" stroke-width="5" fill="none">
        <line x1="0" y1="165" x2="100" y2="165"/>
        <line x1="0" y1="245" x2="100" y2="245"/>
        <line x1="500" y1="165" x2="600" y2="165"/>
        <line x1="500" y1="245" x2="600" y2="245"/>
      </g>
      <polygon class="window" points="150,105 450,105 500,165 500,245 450,315 150,315 100,245 100,165"
               fill="var(--paper)" stroke="var(--gold)" stroke-width="5"/>
    </svg>

    <div class="label">
      <p class="label-product">Clear Glass<br>Concentrate Jar</p>
      <p class="brand-name">582 Resinworks</p>
    </div>

    <p class="volume">5mL</p>
    <p class="product-name">Clear Glass<br>Concentrate Jar</p>

    <div class="cannabis-mark">
      <div class="symbol" role="img" aria-label="Universal cannabis product symbol"></div>
      <p class="caption">MARIJUANA<br>PRODUCT</p>
    </div>
  </section>

  <section class="side">
    <svg width="460" height="380" viewBox="0 0 460 380" aria-hidden="true">
      <g stroke="var(--gold)" stroke-width="5">
        <line x1="0" y1="165" x2="40" y2="165"/>
        <line x1="0" y1="245" x2="40" y2="245"/>
        <line x1="420" y1="165" x2="460" y2="165"/>
        <line x1="420" y1="245" x2="460" y2="245"/>
      </g>
    </svg>
    <p class="mission">
      Here at <em>582 Resinworks</em>, our mission is to be make the purest concentrates available. We strive to fully represent the true essence of the flower through our solventless processes. At 582 Resinworks we only use <em>the finest Michigan grown</em>, pesticide-free flowers for extraction. We pride ourselves on our chemical-free extraction methods, and are constantly innovating to bring better and cleaner concentrates for <em>Medicinal and Recreational use.</em>
    </p>
  </section>

</main>
</body>
</html>
```